Shopguidecraft.com

I've attached two different logo's which I both like and would like to see different designs with each logo. I'm starting a retail consulting business and blog. You can view the start of my project at shopguidecraft.com to get an idea of what I'm creating.
Looking for a design that says creative, strategic and community.
Updates
Hello Everyone,
Thank you for the amazing design so far.
What I Like
- double sided designs, front and back
- one side should be white or green. Customers cannot write on or make notes on an all black card
- Simple, cool, creative is best
My business card will only have the following
- Instagram
- Facebook
- Email
- Website
My new Tag line is
Think Smart. Lead Smart. Work Smart.
My title will be:
Dorian Kessel
Retail Consultant
Please submit 1 or 2 designs with these specifications.
Thank you,
Dorian
Reason: Looking for a few more designs and have now committed the project and it is no longer refundable. Please read brief and follow specific instructions.
Looking for something simple yet creative. Something that may stand out from most cards.
Thank you,
Dorian
Thank you,
Dorian
Target Market(s)
My main target is retail managers and retail businesses that are focused on leadership and people development.
Industry/Entity Type
Retail
Look and feel
Each slider illustrates characteristics of the customer's brand and the style your logo design should communicate.

```html
<!DOCTYPE html>
<html lang="en">
<head>
<meta charset="utf-8">
<title>Shopguidecraft business cards</title>
<link rel="stylesheet" href="https://fonts.googleapis.com/css2?family=Cabin+Condensed:wght@500;600&family=Questrial&display=swap">
<style>
  :root {
    --backdrop: #ece6de;
    --ink: #231f20;
    --brand-green: #2a8a45;
    --lime: #8cc63f;
    --white: #ffffff;
    --mist-green: rgba(140, 198, 63, 0.18);
    --panel-glow: rgba(255, 255, 255, 0.08);
    --icon-grey: #8a9a94;
  }
  * { box-sizing: border-box; margin: 0; padding: 0; }
  html, body { width: 1200px; height: 905px; overflow: hidden; }
  body { background: var(--backdrop); position: relative; font-family: "Cabin Condensed", sans-serif; }

  .card {
    position: absolute; width: 567px; height: 329px;
    background: var(--white); overflow: hidden;
    box-shadow: 0 2px 6px rgba(0, 0, 0, 0.25);
  }
  .card--front { left: 33px; top: 136px; z-index: 2; }
  .card--back  { left: 558px; top: 437px; z-index: 1; }

  .wordmark { position: absolute; font-family: "Questrial", sans-serif; white-space: nowrap; line-height: 1; }
  .brand-dot { position: absolute; border-radius: 50%; background: var(--lime); }

  /* front */
  .front-header { position: absolute; left: 0; top: 0; width: 100%; height: 97px; background: var(--ink); }
  .front-header .brand-dot { left: 11px; top: 22px; width: 52px; height: 52px; }
  .front-header .wordmark { left: 76px; top: 44px; font-size: 36px; color: var(--lime); }
  .social-icon { position: absolute; top: 68px; width: 28px; height: 28px; border-radius: 4px; background: var(--icon-grey); }
  .social-icon--photos { left: 467px; }
  .social-icon--network { left: 507px; }

  .front-panel { position: absolute; left: 0; top: 97px; width: 100%; height: 196px; background: var(--brand-green); overflow: hidden; }
  .panel-mark { position: absolute; left: -4px; top: 7px; width: 196px; height: 196px; border-radius: 50%; background: var(--panel-glow); }
  .holder-name { position: absolute; left: 222px; top: 52px; font-size: 17px; font-weight: 600; color: var(--ink); text-transform: uppercase; }
  .holder-role { position: absolute; left: 230px; top: 79px; font-size: 12px; font-weight: 500; color: var(--white); text-transform: uppercase; }
  .contact { position: absolute; top: 166px; font-size: 11px; font-weight: 500; color: var(--white); text-transform: uppercase; }
  .contact--email { left: 59px; }
  .contact--web { left: 376px; }

  .front-rule { position: absolute; left: 0; top: 293px; width: 100%; height: 2px; background: var(--ink); }
  .front-strip { position: absolute; left: 0; top: 321px; width: 100%; height: 6px; background: var(--brand-green); }

  .tagline { position: absolute; left: 0; width: 100%; height: 26px; font-family: "Questrial", sans-serif; font-size: 18px; text-transform: uppercase; }
  .tagline span { position: absolute; top: 50%; transform: translateY(-50%); white-space: nowrap; }
  .tagline .think { left: 65px; }
  .tagline .lead { left: 224px; color: var(--brand-green); }
  .tagline .work { left: 376px; }
  .card--front .tagline { top: 295px; color: var(--ink); }
  .card--back .tagline { top: 294px; height: 30px; background: var(--ink); color: var(--white); }
  .card--back .tagline .lead { color: var(--lime); }

  /* back */
  .back-mark { position: absolute; left: 190px; top: 36px; width: 230px; height: 230px; border-radius: 50%; background: var(--mist-green); }
  .card--back .brand-dot { left: 122px; top: 120px; width: 68px; height: 68px; }
  .card--back .wordmark { left: 193px; top: 150px; font-size: 38px; color: var(--lime); }
</style>
</head>
<body>
  <section class="card card--front" aria-label="Business card front">
    <header class="front-header">
      <span class="brand-dot"></span>
      <span class="wordmark">Shopguidecraft</span>
      <span class="social-icon social-icon--photos" role="img" aria-label="Photo sharing profile icon"></span>
      <span class="social-icon social-icon--network" role="img" aria-label="Social network profile icon"></span>
    </header>
    <div class="front-panel">
      <span class="panel-mark"></span>
      <p class="holder-name">Dorian Kessel</p>
      <p class="holder-role">Retail Consultant</p>
      <p class="contact contact--email">dorian@shopguidecraft.com</p>
      <p class="contact contact--web">www.shopguidecraft.com</p>
    </div>
    <div class="front-rule"></div>
    <p class="tagline"><span class="think">Think Smart.</span><span class="lead">Lead Smart.</span><span class="work">Work Smart.</span></p>
    <div class="front-strip"></div>
  </section>

  <section class="card card--back" aria-label="Business card back">
    <span class="back-mark"></span>
    <span class="brand-dot"></span>
    <span class="wordmark">Shopguidecraft</span>
    <p class="tagline"><span class="think">Think Smart.</span><span class="lead">Lead Smart.</span><span class="work">Work Smart.</span></p>
  </section>
</body>
</html>
```